Corvane Project Services - Flyer

Project Breif:
I need a single page A4 Capability Statement, which will be used to market our services to prospective clients, both in print and via email PDF.
It needs to look professional and should incorporate the elements I have uploaded into files, these include:
Capability Statement Text
Corvane Services Company Logo
Additional Logo’s (Tools We Use)
Glimmer Bay Pics can be cut into the page
I have included examples of capability statements as a guide to what i am looking for.
Regards
Derek
Engineering Consulting

```html
<!DOCTYPE html>
<html lang="en">
<head>
<meta charset="utf-8">
<title>Corvane Project Services – Capability Statement</title>
<link rel="stylesheet" href="https://fonts.googleapis.com/css2?family=Arimo:wght@400;700&family=Montserrat:wght@400;500;600;700&display=swap">
<style>
:root{
  --backdrop:#bfc0c2;
  --paper:#f7f7f8;
  --blue:#0a7fc7;
  --blue-text:#1478c4;
  --slate:#5e5f62;
  --ink:#2b2b2d;
  --grey-title:#77787b;
  --white:#ffffff;
}
*{margin:0;padding:0;box-sizing:border-box}
html,body{width:979px;height:1200px;overflow:hidden;background:var(--backdrop)}
.sheet{position:absolute;left:155px;top:126px;width:669px;height:947px;background:var(--paper);overflow:hidden;font-family:Arimo,Arial,sans-serif}
.top-band{position:absolute;left:0;top:0;width:326px;height:20px;background:var(--blue)}
.brand{position:absolute;left:86px;top:36px;width:160px;text-align:center}
.brand-dot{width:46px;height:46px;border-radius:50%;background:var(--blue);margin:0 auto 16px}
.brand-name{font-family:Montserrat,sans-serif;font-weight:700;font-size:11.5px;line-height:14px;color:var(--ink);letter-spacing:.5px}
.doc-title{position:absolute;left:424px;top:58px;font-family:Montserrat,sans-serif;font-weight:500;font-size:25px;line-height:25px;letter-spacing:2.5px}
.doc-title .l1{color:var(--blue)}
.doc-title .l2{color:var(--grey-title);letter-spacing:.5px}
.hero-photo{position:absolute;left:0;top:149px;width:669px;height:274px;background:linear-gradient(120deg,#d9c6bd 0%,#eef0f3 35%,#e8ecf2 60%,#c8d6e6 100%)}
.about{position:absolute;left:0;top:276px;width:326px;height:440px;background:rgba(94,95,98,.97);color:var(--white);padding:50px 24px 0 51px;font-size:14.6px;line-height:16.5px}
.about p{margin-bottom:16.5px}
.services{position:absolute;left:353px;top:446px;width:300px}
.services h2{font-family:Montserrat,sans-serif;font-weight:400;font-size:22px;letter-spacing:1px;color:var(--ink);border-left:4px solid var(--blue);padding-left:9px;line-height:22px;margin-bottom:15px}
.services h3{font-family:Montserrat,sans-serif;font-weight:700;font-size:14.5px;color:var(--blue-text);margin-left:12px;line-height:18px;margin-bottom:6px}
.services ul{list-style:none;margin-left:45px;margin-bottom:22px}
.services li{font-size:12.3px;line-height:16.6px;color:var(--ink);position:relative}
.services li::before{content:"";position:absolute;left:-10px;top:6px;width:3.5px;height:3.5px;border-radius:50%;background:var(--blue)}
.tools{position:absolute;left:30px;top:752px;width:280px;font-family:Arimo,Arial,sans-serif;font-weight:700;font-size:14px;color:var(--ink)}
.tool{position:absolute;white-space:nowrap}
.contact-bar{position:absolute;left:0;top:898px;width:669px;height:49px;background:var(--blue);color:var(--white);font-family:Montserrat,sans-serif}
.person{position:absolute;left:45px;top:14px}
.person .name{font-size:12.5px;line-height:14px}
.person .role{font-size:8.5px}
.contact{position:absolute;top:17px;font-size:11.5px;display:flex;align-items:center;gap:6px}
.divider{position:absolute;top:12px;width:1px;height:28px;background:rgba(255,255,255,.6)}
</style>
</head>
<body>
<div class="sheet">
  <div class="top-band"></div>
  <div class="brand">
    <div class="brand-dot"></div>
    <div class="brand-name">CORVANE PROJECT<br>SERVICES</div>
  </div>
  <h1 class="doc-title"><div class="l1">CAPABILITY</div><div class="l2">STATEMENT</div></h1>

  <div class="hero-photo" role="img" aria-label="Photo of colleagues' hands reviewing printed charts and documents at a meeting table"></div>

  <div class="about">
    <p>Corvane Project Services Ltd.is a leading project control consultancy based in Co Cork Ireland</p>
    <p>For over 20 years we have been helping our clients to deliver complex projects and programs throughout mainland Europe.</p>
    <p>We are passionate about empower organisations to achieve their objectives, on time and on budget.</p>
    <p>We are continually innovating, evolving and learning, utilize the latest industry tools and techniques to deliver real value to our clients.</p>
    <p>Our goal is to make successful project delivery more achievable and repeatable.</p>
  </div>

  <section class="services">
    <h2>CORE SERVICES:</h2>
    <h3>PLANNING AND SCHEDULING</h3>
    <ul>
      <li>Tender Planning</li>
      <li>Interactive Planning / Pull Planning</li>
      <li>EPCMV Planning &amp; Scheduling</li>
      <li>Schedule Earned Value Management</li>
      <li>Independent Schedule Quality Assessment</li>
      <li>Schedule Risk Analysis (Monte Carlo)</li>
      <li>Training</li>
    </ul>
    <h3>MANAGEMENT OF RISK</h3>
    <ul>
      <li>Risk Management Policies &amp; Procedures</li>
      <li>Risk Management Strategy</li>
      <li>Risk Registers</li>
      <li>Risk Improvement Planning</li>
      <li>Risk Response and Communication</li>
      <li>Risk Management Training</li>
    </ul>
    <h3>COST CONTROL:</h3>
    <ul>
      <li>Estimating &amp; Forecasting</li>
      <li>Earned Value Analysis</li>
      <li>Progress Reporting</li>
      <li>Cost Risk Analysis</li>
    </ul>
  </section>

  <div class="tools">
    <span class="tool" style="left:14px;top:10px">Tallow Planner</span>
    <span class="tool" style="left:127px;top:10px">Brisk Plan</span>
    <span class="tool" style="left:215px;top:10px">Waypoint Pro</span>
    <span class="tool" style="left:14px;top:56px">Kestra Scheduler</span>
    <span class="tool" style="left:200px;top:56px">RiskFrame</span>
    <span class="tool" style="left:95px;top:102px">Fenwick Gauge</span>
  </div>

  <footer class="contact-bar">
    <div class="person"><div class="name">Derek Holloway</div><div class="role">Managing Director</div></div>
    <div class="contact" style="left:168px">
      <svg width="14" height="14" viewBox="0 0 24 24" fill="none" stroke="#fff" stroke-width="1.6"><path d="M5 3h4l2 5-2.5 1.5a11 11 0 0 0 6 6L16 13l5 2v4a2 2 0 0 1-2 2A16 16 0 0 1 3 5a2 2 0 0 1 2-2z"/></svg>
      +353 (0)871234567</div>
    <div class="divider" style="left:303px"></div>
    <div class="contact" style="left:321px">
      <svg width="14" height="12" viewBox="0 0 24 18" fill="none" stroke="#fff" stroke-width="1.6"><rect x="1" y="1" width="22" height="16"/><path d="M1 1l11 9 11-9"/></svg>
      info@corvaneservices.ie</div>
    <div class="divider" style="left:476px"></div>
    <div class="contact" style="left:491px">
      <svg width="14" height="14" viewBox="0 0 24 24" fill="none" stroke="#fff" stroke-width="1.4"><circle cx="12" cy="12" r="10"/><ellipse cx="12" cy="12" rx="4.5" ry="10"/><path d="M2 12h20M4 6.5h16M4 17.5h16"/></svg>
      www.corvaneservices.ie</div>
  </footer>
</div>
</body>
</html>
```